Vorgan Sports Nutrition Brand needs a Packaging label

Hi all, please see the considerations for our vision.
We need a Golden Ratio packaging label design for new Sports nutrition/supplement brand. I would like to give you a little bit of background about myself and hopefully that will help you in creating the design.
I am myself into fitness. I am 33 years old at the moment and been hitting gyms consistently from 14 years old. I do use supplements of all types that helps with performance and body compositions.
Ideally I would like the brand to be able to resonate with male and female audience. The brand needs to give premium look and feel. Those people who will be associating themselves with the brand should be proud of themselves being a part of the team. That's our ideal customer persona.
In terms of colours we are open to your suggestions but do think that red should be included as a detail colour.
P.S Please check out my Instagram to learn more about ideal customer for the brand. @pelmatovv
When creating the name ''vorgan'' we wanted the name to capture two things. First a feeling that we get when we go to gyms and the feeling is excited. And secondly the name for the product or the industry and that's nutrition. We then shortened the feeling excited to Vorgan for a more catchy name.

The Nutrition information will be sent to add once we pick the design.
The pictures of brands that we admire them are attached.

Please design One label design and just resize for these products. For dimensions please refer to the Print guide attached.
Core Bulk Builder 2.25KG
Tasty Strengthmix 250G
Vigor Lift Prime 120 Tabs
Surge Rush Pre Workout 250G
Branded Shakers

Target Market(s)

Fitness / bodybuilding audience male & female mass market

Industry/Entity Type

Nutrition

Colors

Designer to choose colors to be used in the design.

Requirements
Must have
• Our logo.
• Please find it attached
Nice to have
• The transparent Logo X some where in the background almost like a watermark. In other words like a subconscious clue.
Should not have
• Organic look.

```html
<!DOCTYPE html>
<html lang="en">
<head>
<meta charset="utf-8">
<title>Vorgan Sports Nutrition – Packaging Labels</title>
<link href="https://fonts.googleapis.com/css2?family=Oswald:wght@500;700&family=Roboto+Condensed:wght@700&display=swap" rel="stylesheet">
<style>
  :root {
    --page: #ffffff;
    --label-light: #f4f4f4;
    --pattern-tone: #dcdcdc;
    --label-dark: #2a2a2a;
    --ink: #1b1b1b;
    --brand-red: #c8281f;
    --white: #ffffff;
    --muted: #8a8a8a;
  }
  * { box-sizing: border-box; margin: 0; padding: 0; }
  html, body {
    width: 1200px; height: 884px; overflow: hidden;
    background: var(--page);
  }
  .canvas {
    position: relative; width: 1200px; height: 884px;
  }
  .label {
    position: absolute;
    overflow: hidden;
    background: var(--label-dark);
  }
  .label--gainer { left: 430px; top: 170px; width: 730px; height: 560px; }
  .label--creatine { left: 60px; top: 360px; width: 300px; height: 230px; }

  .label__top {
    position: absolute; left: 0; top: 0; width: 100%; height: 54%;
    background: linear-gradient(160deg, var(--label-light) 0%, var(--pattern-tone) 100%);
  }
  .label__stripe {
    position: absolute; left: 0; top: 54%; width: 100%; height: 1.4%;
    background: var(--brand-red);
  }
  .brand-mark {
    position: absolute; left: 0; width: 100%; top: 24%;
    display: flex; align-items: center; justify-content: center; gap: 0.35em;
    font-family: "Oswald", sans-serif; font-weight: 700;
    color: var(--ink); letter-spacing: 0.04em;
  }
  .brand-mark__square {
    width: 0.6em; height: 0.6em; background: var(--brand-red);
  }
  .label--gainer .brand-mark { font-size: 92px; }
  .label--creatine .brand-mark { font-size: 38px; }

  .product-ribbon {
    position: absolute; left: 50%; transform: translateX(-50%);
    display: flex; align-items: center;
  }
  .product-ribbon__chevron { fill: var(--white); }
  .product-ribbon__name {
    background: var(--brand-red);
    border: 2px solid var(--white);
    color: var(--white);
    font-family: "Oswald", sans-serif; font-weight: 700;
    letter-spacing: 0.05em; white-space: nowrap;
  }
  .label--gainer .product-ribbon { top: 67%; gap: 10px; }
  .label--gainer .product-ribbon__name { font-size: 30px; padding: 2px 22px; }
  .label--creatine .product-ribbon { top: 66%; gap: 4px; }
  .label--creatine .product-ribbon__name { font-size: 12px; padding: 1px 8px; border-width: 1px; }

  .net-weight {
    position: absolute; left: 50%; transform: translateX(-50%);
    display: flex; align-items: center;
    border: 2px solid var(--brand-red); border-radius: 6px;
    font-family: "Roboto Condensed", sans-serif; font-weight: 700;
    color: var(--white); overflow: hidden;
  }
  .net-weight__value { padding: 0 12px; }
  .net-weight__unit { background: var(--white); color: var(--ink); padding: 0 12px; }
  .label--gainer .net-weight { top: 82%; font-size: 26px; }
  .label--creatine .net-weight { top: 80%; font-size: 11px; border-width: 1px; border-radius: 3px; }
  .label--creatine .net-weight__value,
  .label--creatine .net-weight__unit { padding: 0 6px; }

  .supplement-note {
    position: absolute; left: 0; width: 100%; text-align: center;
    font-family: "Roboto Condensed", sans-serif; font-weight: 700;
    color: var(--muted); letter-spacing: 0.03em;
  }
  .label--gainer .supplement-note { top: 92%; font-size: 18px; }
  .label--creatine .supplement-note { top: 91%; font-size: 7px; }
</style>
</head>
<body>
<main class="canvas">

  <section class="label label--creatine" aria-label="Tasty Strengthmix label">
    <div class="label__top" role="img" aria-label="Fine diagonal line pattern in light grey"></div>
    <div class="label__stripe"></div>
    <div class="brand-mark"><span class="brand-mark__square"></span><span>VORGAN</span></div>
    <div class="product-ribbon">
      <svg class="product-ribbon__chevron" width="6" height="12" viewBox="0 0 6 12"><polygon points="0,0 6,6 0,12 2,6"/></svg>
      <span class="product-ribbon__name">TASTY STRENGTHMIX</span>
      <svg class="product-ribbon__chevron" width="6" height="12" viewBox="0 0 6 12"><polygon points="6,0 0,6 6,12 4,6"/></svg>
    </div>
    <div class="net-weight"><span class="net-weight__value">250</span><span class="net-weight__unit">G</span></div>
    <p class="supplement-note">DIETARY SUPPLEMENT</p>
  </section>

  <section class="label label--gainer" aria-label="Core Bulk Builder label">
    <div class="label__top" role="img" aria-label="Fine diagonal line pattern in light grey"></div>
    <div class="label__stripe"></div>
    <div class="brand-mark"><span class="brand-mark__square"></span><span>VORGAN</span></div>
    <div class="product-ribbon">
      <svg class="product-ribbon__chevron" width="16" height="30" viewBox="0 0 16 30"><polygon points="0,0 16,15 0,30 6,15"/></svg>
      <span class="product-ribbon__name">CORE BULK BUILDER</span>
      <svg class="product-ribbon__chevron" width="16" height="30" viewBox="0 0 16 30"><polygon points="16,0 0,15 16,30 10,15"/></svg>
    </div>
    <div class="net-weight"><span class="net-weight__value">2.5</span><span class="net-weight__unit">KG</span></div>
    <p class="supplement-note">DIETARY SUPPLEMENT</p>
  </section>

</main>
</body>
</html>
```